Business card design needed

I run a Beautician studio (for 7 years now)
I offer
- Vestolin Body Sugaring
- Velumi Glow
- Nails
- Facials
- Manicure
- Foot Treatment
It might not be necessary to list all those treatments?
Maybe the link to the Website is sufficient?
I leave that up to you ...
(more info on www.BuffsAndBrowsByMarisol.com.au)
Vestolin BodySugaring is our biggest success, It replaces waxing.
I would like to incorporate the logo into the Business Card.
We had many complaints regarding our old Business Cards as the Phone Number was to small.
On the backside, we would like a "your next Appointment" section.
Looking forward to you Design, cheers ... Marisol
Buffs by Brows by Marisol
14 Merindo Cct 3912 Denmoor
www.BuffsAndBrowsByMarisol.com.au
03 9418 2276

```html
<!DOCTYPE html>
<html lang="en">
<head>
<meta charset="utf-8">
<title>Vestolin Body Sugaring – Business Card</title>
<link rel="stylesheet" href="https://fonts.googleapis.com/css2?family=Cinzel:wght@400;500;600&display=swap">
<style>
  :root {
    --ink: #1d1405;
    --orange: #f49a00;
    --amber: #f8b200;
    --yellow: #fbc90a;
    --pale: #fde56a;
    --bright: #f9e400;
    --sun: #e8661c;
  }
  html, body {
    margin: 0;
    padding: 0;
    width: 1200px;
    height: 740px;
    overflow: hidden;
    background: #ffffff;
  }
  .card {
    position: relative;
    width: 1200px;
    height: 740px;
    overflow: hidden;
    font-family: "Cinzel", serif;
    color: var(--ink);
  }
  .card-background {
    position: absolute;
    inset: 0;
    width: 1200px;
    height: 740px;
  }
  .service-list {
    position: absolute;
    left: 36px;
    top: 34px;
    margin: 0;
    padding: 0;
    list-style: none;
    font-size: 30px;
    line-height: 39px;
    font-weight: 600;
  }
  .brand {
    position: absolute;
    left: 765px;
    top: 40px;
    width: 400px;
    text-align: center;
  }
  .brand-mark {
    display: block;
    width: 160px;
    height: 160px;
    margin: 0 auto 40px;
    border-radius: 50%;
    background: var(--sun);
  }
  .brand-name {
    margin: 0;
    font-size: 27px;
    font-weight: 500;
    letter-spacing: 1px;
    white-space: nowrap;
    color: var(--ink);
  }
  .website {
    position: absolute;
    left: 0;
    width: 1146px;
    top: 426px;
    text-align: center;
    font-size: 30px;
    font-weight: 600;
    margin: 0;
    white-space: nowrap;
  }
  .phone {
    position: absolute;
    left: 14px;
    top: 644px;
    margin: 0;
    font-size: 68px;
    font-weight: 500;
    line-height: 1;
    white-space: nowrap;
  }
  .address {
    position: absolute;
    right: 22px;
    top: 705px;
    margin: 0;
    font-size: 20px;
    font-weight: 600;
    line-height: 1;
    white-space: nowrap;
  }
</style>
</head>
<body>
<main class="card">
  <svg class="card-background" viewBox="0 0 1200 740">
    <defs>
      <linearGradient id="sky" x1="0" y1="0" x2="0" y2="1">
        <stop offset="0" stop-color="var(--orange)"/>
        <stop offset="0.6" stop-color="var(--yellow)"/>
        <stop offset="1" stop-color="var(--yellow)"/>
      </linearGradient>
      <linearGradient id="band" x1="0" y1="0" x2="0" y2="1">
        <stop offset="0" stop-color="var(--pale)"/>
        <stop offset="1" stop-color="var(--yellow)"/>
      </linearGradient>
      <linearGradient id="base" x1="0" y1="0" x2="1" y2="0">
        <stop offset="0" stop-color="var(--orange)"/>
        <stop offset="1" stop-color="var(--amber)"/>
      </linearGradient>
      <radialGradient id="haze">
        <stop offset="0" stop-color="#ffffff" stop-opacity="0.22"/>
        <stop offset="1" stop-color="#ffffff" stop-opacity="0"/>
      </radialGradient>
    </defs>
    <rect class="sky" width="1200" height="740" fill="url(#sky)"/>
    <g role="img" aria-label="Faint decorative swirl ornament, top left">
      <ellipse cx="150" cy="170" rx="230" ry="210" fill="url(#haze)"/>
    </g>
    <path class="wave-light" d="M0,505 C320,560 720,640 1200,475 L1200,740 L0,740 Z" fill="url(#band)"/>
    <path class="wave-line" d="M0,548 C360,600 760,655 1200,520" fill="none" stroke="var(--bright)" stroke-width="6"/>
    <path class="wave-base" d="M0,552 C360,604 760,660 1200,524 L1200,740 L0,740 Z" fill="url(#base)"/>
    <g role="img" aria-label="Faint decorative swirl ornament, bottom right">
      <ellipse cx="1110" cy="620" rx="140" ry="130" fill="url(#haze)"/>
    </g>
  </svg>

  <ul class="service-list">
    <li>Vestolin Body Sugaring</li>
    <li>Velumi Glow</li>
    <li>Nails</li>
    <li>Facials</li>
    <li>Manicure</li>
    <li>Foot Treatment</li>
  </ul>

  <div class="brand">
    <span class="brand-mark"></span>
    <p class="brand-name">Vestolin Body Sugaring</p>
  </div>

  <p class="website">www.BuffsAndBrowsByMarisol.com.au</p>

  <p class="phone">Tel.03 9418 2276</p>

  <p class="address">Buffs by Brows by Marisol 14 Merindo Cct 3912 Denmoor</p>
</main>
</body>
</html>
```